Oil and Gas Letterhead Design Tweak

Simple letterhead information and design tweak.

Please note, we don't want to change the design or logo of the letterhead only the small changes mentioned below.

We need to change the company name up top to "Northvale Petrotek FZCO"

Also, we need to include in the footer the following information. I have attached an image of roughly how we would like to have it displayed in the footer.

Footer Details:

Northvale Petrotek FZCO,
Unit No. 2378, FZCO Trade Hub, level No. 1, K&P 7, Dubai, United Arab Emirates
Northvale Petrotek FZCO is registered as a free zone company under the rules & regulations of FZCO

Target Market(s)

O&G Market

Industry/Entity Type

Oil And Gas

Font styles to use
Sans Serif

Colors

Designer to choose colors to be used in the design.

Requirements
Must have
• Change the company name to Northvale Petrotek FZCO
• Include the footer on the bottom of the first and continuation page
Should not have
• Should not change the design or logo of the letterhead, only the specified changes mentioned above

```html
<!DOCTYPE html>
<html lang="en">
<head>
<meta charset="utf-8">
<title>Northvale Petrotek FZCO – Letterhead</title>
<link rel="stylesheet" href="https://fonts.googleapis.com/css2?family=Figtree:wght@400;600&display=swap">
<style>
  :root {
    --backdrop: #247f83;
    --paper: #ffffff;
    --brand-blue: #0f57a6;
    --brand-red: #e3202a;
    --ink: #24272b;
  }
  * { margin: 0; padding: 0; box-sizing: border-box; }
  html, body { width: 1199px; height: 1200px; overflow: hidden; }
  body {
    position: relative;
    background: var(--backdrop);
    font-family: "Figtree", sans-serif;
    color: var(--ink);
  }
  .sheet {
    position: absolute;
    top: 216px;
    width: 509px;
    height: 719px;
    background: var(--paper);
    overflow: hidden;
  }
  .sheet--first { left: 60px; }
  .sheet--continuation { left: 627px; }

  .bar { position: absolute; display: block; }
  .bar .blue { fill: var(--brand-blue); }
  .bar .red { fill: var(--brand-red); }

  .header-brand {
    position: absolute;
    left: 115px;
    top: 27px;
    display: flex;
    align-items: center;
    gap: 10px;
  }
  .brand-square { width: 18px; height: 18px; background: var(--brand-red); }
  .brand-name { font-size: 18.6px; font-weight: 400; color: var(--ink); white-space: nowrap; }

  .footer {
    position: absolute;
    left: 14px;
    font-size: 7px;
    line-height: 1;
    white-space: nowrap;
  }
  .sheet--first .footer { top: 678px; }
  .sheet--continuation .footer { top: 673px; }
  .footer-name { font-weight: 600; font-size: 7.4px; letter-spacing: 0.1px; }
  .footer-address { display: flex; gap: 10px; margin-top: 4px; }
  .footer-address .sep { font-weight: 600; }
  .footer-note { margin-top: 5px; }

  .corner-brand {
    position: absolute;
    left: 377px;
    top: 680px;
    width: 70px;
    display: flex;
    flex-direction: column;
    align-items: center;
    gap: 3px;
    font-size: 5.6px;
    font-weight: 600;
    line-height: 1.25;
    text-align: center;
    color: var(--ink);
  }
  .corner-brand .brand-square { width: 10px; height: 10px; }
</style>
</head>
<body>

  <section class="sheet sheet--first" aria-label="First page letterhead">
    <svg class="bar top-bars" style="left:0;top:0" width="509" height="9" viewBox="0 0 509 9">
      <polygon class="blue" points="0,0 117,0 112,9 0,9"/>
      <polygon class="red" points="158,0 509,0 509,9 162,9"/>
    </svg>

    <div class="header-brand">
      <span class="brand-square"></span>
      <span class="brand-name">Northvale Petrotek FZCO</span>
    </div>

    <footer class="footer">
      <p class="footer-name">NORTHVALE PETROTEK FZCO</p>
      <p class="footer-address">
        <span>Unit No. 2378</span><span class="sep">|</span>
        <span>FZCO Trade Hub</span><span class="sep">|</span>
        <span>level No. 1, K&amp;P 7</span><span class="sep">|</span>
        <span>Dubai</span><span class="sep">|</span>
        <span>United Arab Emirates</span>
      </p>
      <p class="footer-note">Northvale Petrotek FZCO is registered as a free zone company under the rules &amp; regulations of FZCO</p>
    </footer>

    <svg class="bar bottom-tabs" style="left:369px;top:712px" width="52" height="7" viewBox="0 0 52 7">
      <polygon class="blue" points="5,0 27,0 23,7 0,7"/>
      <polygon class="red" points="30,0 48,0 52,7 27,7"/>
    </svg>
  </section>

  <section class="sheet sheet--continuation" aria-label="Continuation page letterhead">
    <svg class="bar top-tabs" style="left:371px;top:0" width="80" height="15" viewBox="0 0 80 15">
      <polygon class="blue" points="0,0 43,0 36,15 8,15"/>
      <polygon class="red" points="48,0 80,0 72,15 41,15"/>
    </svg>

    <footer class="footer">
      <p class="footer-name">NORTHVALE PETROTEK FZCO</p>
      <p class="footer-address">
        <span>Unit No. 2378</span><span class="sep">|</span>
        <span>FZCO Trade Hub</span><span class="sep">|</span>
        <span>level No. 1, K&amp;P 7</span><span class="sep">|</span>
        <span>Dubai</span><span class="sep">|</span>
        <span>United Arab Emirates</span>
      </p>
      <p class="footer-note">Northvale Petrotek FZCO is registered as a free zone company under the rules &amp; regulations of FZCO</p>
    </footer>

    <div class="corner-brand">
      <span class="brand-square"></span>
      <span>Northvale<br>Petrotek FZCO</span>
    </div>

    <svg class="bar bottom-bars" style="left:0;top:704px" width="509" height="15" viewBox="0 0 509 15">
      <polygon class="blue" points="0,6 378,6 373,15 0,15"/>
      <polygon class="red" points="445,0 509,0 509,15 455,15"/>
    </svg>
  </section>

</body>
</html>
```